Construction business card

I need a new business card, they can connect with my logo, brand.
What we do is residential house , design and build
I like: Navy blue / black
I attached our logo, brand,
and, some idea for business card.

```html
<!DOCTYPE html>
<html lang="en">
<head>
<meta charset="utf-8">
<title>Harlow Building Group – Business Card</title>
<link href="https://fonts.googleapis.com/css2?family=Varela+Round&family=Arimo:wght@400&display=swap" rel="stylesheet">
<style>
  :root {
    --bg-top: #aec9cc;
    --bg-bottom: #dcfbfb;
    --brand-blue: #3d82c9;
    --brand-navy: #020a26;
    --card-white: #ffffff;
    --text-dark: #222222;
    --text-muted: #333333;
  }
  * { box-sizing: border-box; margin: 0; padding: 0; }
  html, body {
    width: 1200px;
    height: 1200px;
    overflow: hidden;
  }
  body {
    background: linear-gradient(180deg, var(--bg-top), var(--bg-bottom));
    display: flex;
    flex-direction: column;
    align-items: center;
    justify-content: center;
    gap: 80px;
    font-family: "Arimo", Arial, sans-serif;
  }
  .card {
    width: 700px;
    height: 427px;
    position: relative;
    box-shadow: 0 18px 40px rgba(20, 50, 60, 0.18);
  }

  /* Front side */
  .card--front {
    background: var(--card-white);
  }
  .front__brand {
    position: absolute;
    top: 92px;
    left: 0;
    right: 0;
    text-align: center;
    font-family: "Varela Round", sans-serif;
    color: var(--brand-blue);
    font-size: 34px;
    letter-spacing: 1px;
    line-height: 1.15;
  }
  .front__brand-line { display: block; }
  .front__brand-line--small { font-size: 22px; letter-spacing: 3px; }
  .front__person {
    position: absolute;
    top: 262px;
    right: 390px;
    text-align: right;
  }
  .person__name {
    font-family: "Varela Round", sans-serif;
    color: var(--brand-blue);
    font-size: 34px;
    letter-spacing: 1px;
    line-height: 1;
  }
  .person__role {
    font-size: 14px;
    color: var(--text-muted);
    margin-top: 4px;
  }
  .front__divider {
    position: absolute;
    left: 340px;
    top: 232px;
    width: 3px;
    height: 142px;
    background: var(--brand-blue);
  }
  .front__contacts {
    position: absolute;
    left: 372px;
    top: 238px;
    list-style: none;
    font-size: 16px;
    color: var(--text-dark);
  }
  .contact {
    display: flex;
    align-items: flex-start;
    gap: 14px;
    margin-bottom: 7px;
    line-height: 1.3;
  }
  .contact--address { margin-bottom: 12px; }
  .contact__icon {
    width: 18px;
    height: 18px;
    flex: none;
    margin-top: 1px;
    color: var(--brand-blue);
  }

  /* Back side */
  .card--back {
    background: var(--brand-navy);
  }
  .back__brand {
    position: absolute;
    left: 60px;
    top: 84px;
    font-family: "Varela Round", sans-serif;
    color: var(--card-white);
    font-size: 40px;
    letter-spacing: 1px;
    line-height: 1.15;
  }
  .back__brand-line { display: block; }
  .back__brand-line--small { font-size: 25px; letter-spacing: 3px; }
</style>
</head>
<body>
  <section class="card card--front" aria-label="Business card front">
    <div class="front__brand">
      <span class="front__brand-line">HARLOW</span>
      <span class="front__brand-line front__brand-line--small">BUILDING GROUP</span>
    </div>

    <div class="front__person">
      <p class="person__name">Sam Carter</p>
      <p class="person__role">Manager</p>
    </div>

    <div class="front__divider"></div>

    <ul class="front__contacts">
      <li class="contact contact--address">
        <svg class="contact__icon" viewBox="0 0 24 24" aria-hidden="true">
          <circle cx="12" cy="11" r="8" fill="none" stroke="currentColor" stroke-width="3"/>
          <circle cx="12" cy="11" r="2.5" fill="currentColor"/>
        </svg>
        <span>42 Harbourview Street,<br>Eastfield, Vic 3190</span>
      </li>
      <li class="contact">
        <svg class="contact__icon" viewBox="0 0 24 24" aria-hidden="true">
          <path d="M5 3l4 1 1 5-2 2c1.5 3 3 4.5 6 6l2-2 5 1 1 4-3 2C10 21 3 14 3 6z" fill="currentColor"/>
        </svg>
        <span>0400 555 018</span>
      </li>
      <li class="contact">
        <svg class="contact__icon" viewBox="0 0 24 24" aria-hidden="true">
          <rect x="2" y="5" width="20" height="14" fill="none" stroke="currentColor" stroke-width="2"/>
          <path d="M2 5l10 8 10-8" fill="none" stroke="currentColor" stroke-width="2"/>
        </svg>
        <span>info@harlowbuilding.com.au</span>
      </li>
      <li class="contact">
        <svg class="contact__icon" viewBox="0 0 24 24" aria-hidden="true">
          <circle cx="12" cy="12" r="10" fill="none" stroke="currentColor" stroke-width="2"/>
          <ellipse cx="12" cy="12" rx="4.5" ry="10" fill="none" stroke="currentColor" stroke-width="1.6"/>
          <path d="M2 12h20M4 7h16M4 17h16" stroke="currentColor" stroke-width="1.6"/>
        </svg>
        <span>www.harlowbuilding.com.au</span>
      </li>
    </ul>
  </section>

  <section class="card card--back" aria-label="Business card back">
    <div class="back__brand">
      <span class="back__brand-line">HARLOW</span>
      <span class="back__brand-line back__brand-line--small">BUILDING GROUP</span>
    </div>
  </section>
</body>
</html>
```